Bureau for Venture and Discovery Needs a Graphically Designed Powerpoint Template

We are from Bureau for Venture and Discovery (BVaD), part of a medical school. BVaD contributes to the medical school by overseeing and managing intellectual property generated by researchers at the medical school, and also works to ensure optimal commercial outcomes for all inventions arising from the medical school. We want a graphically designed powerpoint presentation template to describe how BVaD is involved in a researcher’s journey to major scientific contributions. The journey should be represented in the form of a main road (or pathway). Along the main road, there will be smaller roads branching out, each representing one of the researcher’s major scientific contributions. We will be inputting text details of each major scientific contribution near each of the small road branches. The smaller road branches will also need to be removable / editable. This is because we might need to send the template to different researchers to input details of their major scientific contributions, and each researcher will have a different number of them. Hence, you can possibly place around 6 branches along the main road, but we want to be able to remove the branches should we need to. Removal of the branches (design elements) should still result in a seamless image in powerpoint. We also want to be able to add and edit text in the design template. The start of the main road should contain a placeholder for us to place the researcher’s photo. The end of the road will lead to one of the major scientific contributions. Please see the uploaded sketch to have an idea of what we are looking to get. We welcome deviations and changes to the design as shown from the sketch, as long as the design is able to convey what we have described above. As this powerpoint template will be used for presentation to the senior management, we need it to look beautiful yet professional.

Target Market(s)

Researcher, Scientist

Industry/Entity Type

School

Font styles to use
Serif
Sans Serif

Requirements
Must have
• A main road or pathway as mentioned in the project description.
Nice to have
• We will leave the "nice to haves" to be decided by the designer.
Should not have
• Trees

```html
<!DOCTYPE html>
<html lang="en">
<head>
<meta charset="UTF-8">
<title>BVaD services / a researcher's journey</title>
<link href="https://fonts.googleapis.com/css2?family=Playfair+Display:wght@400;700;900&family=Open+Sans:wght@300;400;700&display=swap" rel="stylesheet">
<style>
  :root {
    --ink: #1a1a1a;
    --blue: #1a66b2;
    --teal: #2aa8a4;
    --road-start: #2272ae;
    --road-end: #2aa8a4;
    --grey-label: #b3b3b3;
    --body-text: #555555;
    --card-bg: #ffffff;
    --bg-top: #ffffff;
    --bg-bottom: #f0f0f0;
    --node: #333333;
  }
  * { margin: 0; padding: 0; box-sizing: border-box; }
  html, body { width: 1200px; height: 675px; overflow: hidden; }
  body {
    position: relative;
    background: radial-gradient(ellipse at 30% 20%, var(--bg-top) 0%, var(--bg-bottom) 100%);
    font-family: "Open Sans", Arial, sans-serif;
    color: var(--ink);
  }
  .slide-title {
    position: absolute; left: 56px; top: 52px;
    font-family: "Playfair Display", Georgia, serif;
  }
  .slide-title .title-main { display: block; font-weight: 400; font-size: 49px; line-height: 56px; }
  .slide-title .title-sub {
    display: block; font-weight: 900; font-size: 50px; line-height: 58px;
    background: linear-gradient(90deg, var(--blue) 0%, var(--teal) 100%);
    -webkit-background-clip: text; background-clip: text; color: transparent;
  }
  .researcher-panel {
    position: absolute; left: 54px; top: 182px; width: 161px; height: 425px;
    background: linear-gradient(180deg, var(--blue) 0%, var(--teal) 100%);
    border-radius: 14px 0 14px 0;
    color: #fff; padding: 17px 16px 0 17px;
  }
  .researcher-photo {
    width: 127px; height: 126px;
    background: linear-gradient(160deg, #d9dde2 0%, #c98a70 55%, #e6e9ec 100%);
  }
  .researcher-name {
    margin-top: 12px; font-family: "Playfair Display", Georgia, serif;
    font-weight: 700; font-size: 17px; line-height: 22px;
  }
  .panel-rule { width: 32px; height: 2px; background: #fff; margin-top: 34px; }
  .panel-heading { font-weight: 700; font-size: 11.5px; margin-top: 5px; line-height: 15px; }
  .panel-text { font-weight: 300; font-size: 11.5px; line-height: 15px; }
  .panel-list { list-style: none; }
  .panel-list li { font-weight: 300; font-size: 11.5px; line-height: 15px; position: relative; padding-left: 28px; }
  .panel-list li::before { content: "•"; position: absolute; left: 0; }
  .panel-rule.second { margin-top: 19px; }
  .main-road {
    position: absolute; left: 231px; top: 392px; width: 915px; height: 4px;
    background: linear-gradient(90deg, var(--road-start) 0%, var(--road-end) 100%);
  }
  .timeline { position: absolute; left: 0; top: 0; width: 1200px; height: 675px; }
  .phase-label {
    position: absolute; font-family: "Playfair Display", Georgia, serif;
    color: var(--grey-label); font-size: 17px; line-height: 21px;
  }
  .phase-label strong { font-weight: 700; display: block; }
  .milestone-card {
    position: absolute; width: 176px; height: 171px; background: var(--card-bg);
    box-shadow: 2px 2px 5px rgba(0,0,0,0.28); padding: 11px 8px 0 11px;
  }
  .milestone-card h3 {
    font-family: "Playfair Display", Georgia, serif; font-weight: 700;
    font-size: 12px; line-height: 15px; color: #222; margin-bottom: 15px;
  }
  .milestone-card p {
    font-weight: 300; font-size: 11.2px; line-height: 15px; color: var(--body-text);
    white-space: nowrap;
  }
  .milestone-card svg { position: absolute; right: 11px; bottom: 11px; }
</style>
</head>
<body>
  <h1 class="slide-title">
    <span class="title-main">BVaD services</span>
    <span class="title-sub">/ a researcher’s journey</span>
  </h1>

  <aside class="researcher-panel">
    <div class="researcher-photo" role="img" aria-label="Researcher's portrait photo placeholder"></div>
    <div class="researcher-name">Researcher’s<br>name PhD.</div>
    <div class="panel-rule"></div>
    <div class="panel-heading">Institution</div>
    <div class="panel-text">Lorem ipsum</div>
    <div class="panel-rule second"></div>
    <div class="panel-heading">Research subjects</div>
    <ul class="panel-list">
      <li>Lorem ipsum</li><li>Lorem ipsum</li><li>Lorem ipsum</li>
    </ul>
  </aside>

  <div class="main-road"></div>

  <svg class="timeline" viewBox="0 0 1200 675" aria-hidden="true">
    <g stroke="#333" fill="none" stroke-width="0.9">
      <line x1="265" y1="394" x2="265" y2="436"/>
      <line x1="492" y1="394" x2="492" y2="355"/>
      <line x1="720" y1="394" x2="720" y2="436"/>
      <line x1="949" y1="394" x2="949" y2="355"/>
      <g><circle cx="265" cy="394" r="11"/><circle cx="265" cy="394" r="8"/></g>
      <g><circle cx="492" cy="394" r="11"/><circle cx="492" cy="394" r="8"/></g>
      <g><circle cx="720" cy="394" r="11"/><circle cx="720" cy="394" r="8"/></g>
      <g><circle cx="949" cy="394" r="11"/><circle cx="949" cy="394" r="8"/></g>
    </g>
    <g fill="#333">
      <circle cx="265" cy="394" r="4"/><circle cx="492" cy="394" r="4"/>
      <circle cx="720" cy="394" r="4"/><circle cx="949" cy="394" r="4"/>
    </g>
  </svg>

  <div class="phase-label" style="left:229px; top:332px;">Phase 1<strong>/Lorem ipsum</strong></div>
  <div class="phase-label" style="left:676px; top:332px;">Phase 2<strong>/Lorem ipsum</strong></div>

  <article class="milestone-card" style="left:254px; top:436px;">
    <h3>BVaD xyz<br>Project</h3>
    <p>Lorem ipsum dolor sit amet,<br>consectetur adipiscing elit.<br>Ut ornare nunc nec lectus<br>aliquam, eget accumsan<br>felis fermentum.</p>
    <svg width="28" height="26" viewBox="0 0 28 26" fill="none" stroke="#1a66b2" stroke-width="1.2" stroke-linejoin="round">
      <path d="M27 1 L1 11 L11 15 L15 25 Z"/><path d="M11 15 L27 1"/>
    </svg>
  </article>

  <article class="milestone-card" style="left:481px; top:185px;">
    <h3>Major scientific<br>constribution</h3>
    <p>Lorem ipsum dolor sit amet,<br>consectetur adipiscing elit.<br>Ut ornare nunc nec lectus<br>aliquam, eget accumsan<br>felis fermentum.</p>
    <svg width="24" height="26" viewBox="0 0 24 26" fill="none" stroke="#2a9a9e" stroke-width="1.2">
      <path d="M2 1 V25"/><path d="M2 3 H22 L18 8 L22 13 H2"/>
    </svg>
  </article>

  <article class="milestone-card" style="left:709px; top:436px;">
    <h3>Major scientific<br>constribution</h3>
    <p>Lorem ipsum dolor sit amet,<br>consectetur adipiscing elit.<br>Ut ornare nunc nec lectus<br>aliquam, eget accumsan<br>felis fermentum.</p>
    <svg width="24" height="26" viewBox="0 0 24 26" fill="none" stroke="#2a9a9e" stroke-width="1.2">
      <path d="M2 1 V25"/><path d="M2 3 H22 L18 8 L22 13 H2"/>
    </svg>
  </article>

  <article class="milestone-card" style="left:937px; top:185px;">
    <h3>Major scientific<br>constribution</h3>
    <p>Lorem ipsum dolor sit amet,<br>consectetur adipiscing elit.<br>Ut ornare nunc nec lectus<br>aliquam, eget accumsan<br>felis fermentum.</p>
    <svg width="24" height="26" viewBox="0 0 24 26" fill="none" stroke="#2a9a9e" stroke-width="1.2">
      <path d="M2 1 V25"/><path d="M2 3 H22 L18 8 L22 13 H2"/>
    </svg>
  </article>
</body>
</html>
```